Brine KLV - Website

Brine KLV is a online marketing solutions Agency, working with top partners within the industry to deliver online customers to Digital campaigns.

Our current site is www.brineklv.example (Apart from the logo, there is NOTHING we like about this site - please do not repeat anything from this site)

Specification of website:

- Modern, and light refreshing look. Corporate and neutral designs.

-Keep our logo - colour theme: Green/grey - hint of Orange/Blue

- The only text we would like on the Homepage is: Performance based online marketing specialists, driving incremental sales globally

and...

These are headings we would like people to do: Affiliate Marketing, Email marketing, Lead Generation, Social media marketing, Search Engine Marketing, Incentive Marketing (there is no need for the detailed text of these topics to be on front page, these can be linked into another page for those who seeks further info)

Images: Have images to show what we do.. keep it neat and professional/simple and stylish.

Please contact us if you have any questions at all.

Thank you for taking time our with our project!

Good luck all!

Regards

Brine KLV
Updates

Hello Designers,

Thank you to all who have taken time out working on our project. We have been very happy with the quality and level of prompt feedback.

Unfortunately we could only choose one, and MoonVex's designed is most suited for our company branding. So, Congratulations MoonVex.

Once again, thank you all.

Kindest regards,

Brine KLV

Target Market(s)

Clients: Fizzo, Torvik, Lunco, pelbet.example, Varnell Hotel...

Industry/Entity Type

Marketing

Requirements
Must have
• User friendly
Nice to have
• We operate Internationally, so a generic feel for EU/UK/US would be ideal...
Should not have
• Should not look like www.brineklv.example

```html
<!DOCTYPE html>
<html lang="en">
<head>
<meta charset="utf-8">
<title>Brine KLV – Online Marketing</title>
<link rel="stylesheet" href="https://fonts.googleapis.com/css2?family=Arimo:wght@400;700&family=Gelasio:wght@400&display=swap">
<style>
  :root {
    --green: #7cb52a;
    --green-dark: #5e9a18;
    --green-light: #a6d04f;
    --green-text: #8cbf3f;
    --orange: #f7931e;
    --orange-light: #f8c48c;
    --grey-bg: #efefef;
    --grey-foot: #e2e2e2;
    --grey-line: #d6d6d6;
    --text: #2a2a2a;
    --text-soft: #555;
    --white: #ffffff;
    --blue: #2b7bc0;
  }
  * { box-sizing: border-box; margin: 0; padding: 0; }
  html, body { width: 1200px; height: 852px; overflow: hidden; }
  body {
    position: relative;
    font-family: "Arimo", Arial, sans-serif;
    color: var(--text);
    background: var(--grey-bg);
  }
  .page-top {
    position: absolute; left: 0; top: 0; width: 1200px; height: 460px;
    background: linear-gradient(180deg, #d6ecb8 0%, #eef7e2 40%, #ffffff 75%, #f6f6f6 100%);
  }
  .logo {
    position: absolute; left: 92px; top: 36px;
    display: flex; align-items: center; gap: 12px;
  }
  .logo-name {
    font-family: "Gelasio", Georgia, serif;
    font-size: 50px; color: var(--green); line-height: 1;
  }
  .logo-dot { width: 34px; height: 34px; border-radius: 50%; background: #c9c9c9; }
  .quote-tab {
    position: absolute; left: 904px; top: 0; width: 180px; height: 40px;
    background: var(--orange); border-radius: 0 0 6px 6px;
    display: flex; align-items: center; justify-content: center; gap: 10px;
    color: var(--white); font-family: "Gelasio", Georgia, serif; font-weight: 400; font-size: 20px;
    text-decoration: none; white-space: nowrap;
  }
  .main-nav {
    position: absolute; left: 360px; top: 84px; width: 754px; height: 44px;
    background: linear-gradient(180deg, var(--green-light), var(--green-dark));
    border-radius: 6px;
    display: flex; align-items: center; justify-content: space-between;
    padding: 0 18px 0 4px;
  }
  .main-nav a {
    color: var(--white); text-decoration: none; white-space: nowrap;
    font-family: "Gelasio", Georgia, serif; font-size: 17px;
    height: 40px; display: flex; align-items: center; padding: 0 4px;
  }
  .main-nav a.active { background: var(--orange); border-radius: 4px; padding: 0 26px; }
  .hero {
    position: absolute; left: 80px; top: 140px; width: 1034px; height: 316px;
    background: var(--white); border-radius: 14px 14px 0 0;
  }
  .hero-arrow { position: absolute; top: 118px; }
  .hero-arrow.prev { left: 18px; }
  .hero-arrow.next { right: 18px; }
  .hero-title {
    position: absolute; left: 76px; top: 94px; white-space: nowrap;
    font-family: "Gelasio", Georgia, serif; font-weight: 400;
    font-size: 33px; line-height: 42px; color: var(--green-text);
  }
  .hero-title .accent { color: var(--orange); }
  .hero-visual {
    position: absolute; left: 684px; top: 40px; width: 200px; height: 240px;
    border-radius: 20px;
    background: radial-gradient(circle at 50% 40%, #9fd16a 0%, #7fb2e0 45%, #f6b15c 75%, #ffffff 100%);
    opacity: 0.85;
  }
  .services {
    position: absolute; left: 66px; top: 504px; display: flex; gap: 14px;
  }
  .service-card {
    position: relative; width: 252px; height: 206px;
    background: var(--white); border: 2px solid var(--orange-light); border-radius: 14px;
  }
  .service-icon { position: absolute; left: 16px; top: 14px; width: 44px; height: 44px; }
  .service-title {
    position: absolute; left: 76px; top: 10px; white-space: nowrap;
    font-family: "Gelasio", Georgia, serif; font-weight: 400; font-size: 21px; line-height: 28px; color: var(--text);
  }
  .service-text {
    position: absolute; left: 16px; top: 80px; width: 214px;
    font-size: 12.5px; line-height: 16px; color: var(--text);
  }
  .more-info {
    position: absolute; left: 14px; top: 186px; width: 102px; height: 26px;
    background: linear-gradient(180deg, var(--green-light), var(--green-dark));
    border-radius: 13px; color: var(--white); text-decoration: none; white-space: nowrap;
    font-family: "Gelasio", Georgia, serif; font-size: 14px;
    display: flex; align-items: center; padding-left: 12px; gap: 8px;
  }
  .slider-dots { position: absolute; left: 1070px; top: 730px; display: flex; gap: 6px; }
  .slider-dots span { width: 18px; height: 18px; border-radius: 50%; }
  .slider-dots .on { background: var(--orange); }
  .slider-dots .off { background: var(--green); }
  .site-footer {
    position: absolute; left: 0; top: 762px; width: 1200px; height: 90px;
    background: var(--grey-foot); border-top: 1px solid var(--grey-line);
  }
  .footer-nav {
    position: absolute; left: 0; top: 28px; width: 1200px;
    display: flex; justify-content: center; gap: 22px; font-size: 12px; color: var(--text-soft);
  }
  .footer-nav a { color: var(--text-soft); text-decoration: none; }
  .copyright {
    position: absolute; left: 0; top: 58px; width: 1200px; text-align: center;
    font-size: 12px; color: var(--text-soft);
  }
</style>
</head>
<body>
  <div class="page-top"></div>

  <header>
    <div class="logo"><span class="logo-name">Brine KLV</span><span class="logo-dot"></span></div>
    <a class="quote-tab" href="#">
      <svg width="18" height="20" viewBox="0 0 18 20" aria-hidden="true"><path d="M4 1 L7 1 L8 6 L6 8 Q8 12 11 14 L13 12 L17 13 L17 17 Q16 19 13 19 Q2 15 1 4 Q1 1 4 1 Z" fill="#fff"/></svg>
      Get a Quote !
    </a>
    <nav class="main-nav">
      <a class="active" href="#">home</a>
      <a href="#">about us</a>
      <a href="#">what we do</a>
      <a href="#">our work</a>
      <a href="#">work with us</a>
      <a href="#">contact us</a>
    </nav>
  </header>

  <section class="hero">
    <svg class="hero-arrow prev" width="22" height="44" viewBox="0 0 22 44" aria-hidden="true"><path d="M18 3 L4 22 L18 41" fill="none" stroke="#cfcfcf" stroke-width="4"/></svg>
    <h1 class="hero-title">Performance based<br><span class="accent">ONLINE MARKETING</span> specialists,<br>driving incremental sales globally</h1>
    <div class="hero-visual" role="img" aria-label="Illustration of three colourful figures standing on joined puzzle pieces"></div>
    <svg class="hero-arrow next" width="22" height="44" viewBox="0 0 22 44" aria-hidden="true"><path d="M4 3 L18 22 L4 41" fill="none" stroke="#cfcfcf" stroke-width="4"/></svg>
  </section>

  <main class="services">
    <article class="service-card">
      <svg class="service-icon" viewBox="0 0 44 44" aria-hidden="true"><circle cx="22" cy="22" r="20" fill="var(--blue)"/><rect x="10" y="15" width="24" height="16" fill="#fff"/><path d="M10 15 L22 25 L34 15" fill="none" stroke="var(--blue)" stroke-width="2"/></svg>
      <h2 class="service-title">Email<br>Marketing</h2>
      <p class="service-text">People aged between 18 and 24 spend an average of 31 hours a month checking their inboxes. Study has shown that email marketing will remain an essential tool in marketing for a long time to come.</p>
      <a class="more-info" href="#">more info <svg width="8" height="10" viewBox="0 0 8 10" aria-hidden="true"><path d="M0 0 L8 5 L0 10 Z" fill="#fff"/></svg></a>
    </article>
    <article class="service-card">
      <svg class="service-icon" viewBox="0 0 44 44" aria-hidden="true"><rect x="16" y="8" width="12" height="8" rx="2" fill="none" stroke="#6b3a1a" stroke-width="3"/><rect x="5" y="14" width="34" height="24" rx="3" fill="#8a4a20"/><rect x="19" y="22" width="6" height="5" fill="#e8b04a"/></svg>
      <h2 class="service-title">Lead<br>Generation</h2>
      <p class="service-text">This channel remains one of the most powerful acquisition methods in marketing. At Brine KLV we understand that to harness the true power of lead gen you have to balance quantity with quality.</p>
      <a class="more-info" href="#">more info <svg width="8" height="10" viewBox="0 0 8 10" aria-hidden="true"><path d="M0 0 L8 5 L0 10 Z" fill="#fff"/></svg></a>
    </article>
    <article class="service-card">
      <svg class="service-icon" viewBox="0 0 44 44" aria-hidden="true"><rect x="6" y="20" width="8" height="18" fill="var(--green)"/><rect x="16" y="8" width="8" height="30" fill="var(--blue)"/><rect x="26" y="16" width="8" height="22" fill="var(--orange)"/><rect x="4" y="38" width="34" height="2" fill="#999"/></svg>
      <h2 class="service-title">Incentive<br>Marketing</h2>
      <p class="service-text">It is a $46bn+ a year industry because it drives very high volumes of traffic at low costs and should never be ruled out without careful consideration.</p>
      <a class="more-info" href="#">more info <svg width="8" height="10" viewBox="0 0 8 10" aria-hidden="true"><path d="M0 0 L8 5 L0 10 Z" fill="#fff"/></svg></a>
    </article>
    <article class="service-card">
      <svg class="service-icon" viewBox="0 0 44 44" aria-hidden="true"><circle cx="22" cy="22" r="18" fill="#d9d9d9"/></svg>
      <h2 class="service-title">Social Media<br>Marketing</h2>
      <p class="service-text">Brine KLV and its partners have consistently been at the forefront of this new media, helping to pioneer new monetisation methods and strategies.</p>
      <a class="more-info" href="#">more info <svg width="8" height="10" viewBox="0 0 8 10" aria-hidden="true"><path d="M0 0 L8 5 L0 10 Z" fill="#fff"/></svg></a>
    </article>
  </main>

  <div class="slider-dots"><span class="on"></span><span class="off"></span></div>

  <footer class="site-footer">
    <nav class="footer-nav">
      <a href="#">Home</a><span>|</span>
      <a href="#">About Us</a><span>|</span>
      <a href="#">What we Do</a><span>|</span>
      <a href="#">Our work</a><span>|</span>
      <a href="#">Work with us</a><span>|</span>
      <a href="#">Contact Us</a>
    </nav>
    <p class="copyright">Copyright © 2010 Brine KLV. All Rights Reserved.</p>
  </footer>
</body>
</html>
```